Carver Lindqvist Group Business Cards

We have a new logo, and want to design new business cards with it. We are 21 years in business, and want a fresh but professional look, so not a lot of extra stuff on the card. We are a recruiting and staffing firm focused on placing accounting and finance professionals in the Dallas TX area. I've attached our new logo that should be displayed on the cards. Here is what I think we want on the cards:
Ray Pemberly, CPA
Partner and Managing Director
8282 Orchard Vale Rd.
Suite 610
Dallas, TX 75391
O 214-555-0184
M 214-555-0237
ray@carverlindqvist.example
www.carverlindqvist.example

```html
<!DOCTYPE html>
<html lang="en">
<head>
<meta charset="utf-8">
<title>Carver Lindqvist Group – Business Card</title>
<link rel="stylesheet" href="https://fonts.googleapis.com/css2?family=Arimo:wght@400;700&display=swap">
<style>
  :root {
    --bg: #e9ebef;
    --card-white: #ffffff;
    --blue-deep: #2b4fb4;
    --blue-soft: #6b90d2;
    --blue-ink: #2d4fb8;
    --grey-text: #8a8d93;
    --rule: #9bb3e0;
  }
  * { margin: 0; padding: 0; box-sizing: border-box; }
  html, body {
    width: 1200px; height: 780px; overflow: hidden;
    background: var(--bg);
    font-family: "Arimo", Arial, sans-serif;
  }
  .card {
    position: absolute; left: 80px; top: 93px;
    width: 1040px; height: 594px;
    background: var(--card-white);
    overflow: hidden;
    box-shadow: 0 10px 30px rgba(0,0,0,0.15);
  }
  .card-shapes { position: absolute; inset: 0; }
  .brand {
    position: absolute; left: 420px; top: 104px;
    display: flex; align-items: center; gap: 14px;
  }
  .brand-mark { width: 30px; height: 30px; background: var(--blue-ink); flex: none; }
  .brand-name {
    font-size: 32px; line-height: 36px; font-weight: 700; color: var(--blue-ink);
    text-transform: uppercase; letter-spacing: 0.5px;
  }
  .brand-rule {
    position: absolute; left: 464px; top: 196px;
    width: 320px; height: 2px; background: var(--rule);
  }
  .contact { position: absolute; left: 265px; top: 300px; color: var(--grey-text); }
  .contact-name {
    font-size: 27px; font-weight: 400; color: var(--blue-ink); text-transform: uppercase;
    letter-spacing: 0.5px;
  }
  .contact-title { font-size: 20px; margin-top: 2px; }
  .contact-address { font-size: 20px; line-height: 27px; margin-top: 22px; }
  .contact-lines { list-style: none; margin-top: 14px; font-size: 20px; line-height: 28px; }
  .contact-lines li { display: flex; align-items: center; gap: 10px; }
  .contact-lines svg { width: 18px; height: 18px; flex: none; }
  .website {
    position: absolute; right: 36px; bottom: 58px;
    color: #ffffff; font-size: 19px; letter-spacing: 0.3px;
  }
</style>
</head>
<body>
  <main class="card">
    <svg class="card-shapes" viewBox="0 0 1040 594" preserveAspectRatio="none" aria-hidden="true">
      <path d="M0 0 H200 Q60 300 190 594 H0 Z" fill="var(--blue-deep)"/>
      <path d="M1040 0 H800 Q980 260 640 594 H1040 Z" fill="var(--blue-soft)"/>
    </svg>

    <div class="brand">
      <span class="brand-mark"></span>
      <span class="brand-name">Carver Lindqvist<br>Group</span>
    </div>
    <div class="brand-rule"></div>

    <section class="contact">
      <h1 class="contact-name">Ray Pemberly, CPA</h1>
      <p class="contact-title">Partner and Managing Director</p>
      <p class="contact-address">8282 Orchard Vale Rd., Suite 610<br>Dallas, TX 75391</p>
      <ul class="contact-lines">
        <li>
          <svg viewBox="0 0 18 18"><rect width="18" height="18" rx="2" fill="var(--blue-ink)"/><path d="M4 12c0-4 2-6 5-6s5 2 5 6z M3 7c2-2 10-2 12 0" fill="none" stroke="#fff" stroke-width="1.6"/></svg>
          214-555-0184
        </li>
        <li>
          <svg viewBox="0 0 18 18"><rect x="3" y="1" width="12" height="16" rx="1" fill="none" stroke="var(--blue-ink)" stroke-width="1.6"/></svg>
          214-555-0237
        </li>
        <li>
          <svg viewBox="0 0 18 18"><rect width="18" height="18" rx="2" fill="var(--blue-ink)"/><path d="M3 5l6 5 6-5M3 13l4-4M15 13l-4-4" fill="none" stroke="#fff" stroke-width="1.4"/></svg>
          ray@carverlindqvist.example
        </li>
      </ul>
    </section>

    <p class="website">www.carverlindqvist.example</p>
  </main>
</body>
</html>
```